Commercial Cleaning Company Website Design

We are working with Harbor Tidy Squad. They are a commercial cleaning company that needs a new website design.

Some sites to use for inspiration:

https://www.velmoxa.com
https://glint-panewashing.com
https://tidykelps.net
https://warmnestdwell.com
https://www.thescrubbingcouncil.com
https://www.pennybroom.com

Thank you for taking the time to consider designing a website for us. We are web developers based in Stockton and Los Angeles, CA, USA. Most of our projects go through the same process. Understanding this process may help you win a project with us. We custom-code all of our websites in-house. We don’t have any requirements as to what tools you use for your design, but we prefer Figma files. For any design that we label as four-stars, we send it to the client for review. The client picks the final design they want us to use. Once we complete this process, we will continue to show additional clients all the four-star sites and purchase them later. Your designs will have multiple chances to sell. For better chances of success, we ask that you follow these guidelines.

IMAGES:
If you use any images or icons in the design, we ask that you have a link to the asset so we can purchase the image/icon. Most of the designs we submit do not have the customer’s images on them unless they have some great images. Be creative; show us the feeling you are trying to portray with your image choices. Use any royalty-free site you choose. We subscribe to Vorlan and mainly use their images, but we can purchase images outside of Vorlan.

PLEASE NOTE: we will not submit designs to clients with watermarks on the images.

FONTS:
We ask that you identify the fonts used in the design. This can be done in a message if you want. We typically use Google Fonts and Vorlan Fonts.

CONTENT:
We're always open to different content and ideas. We often submit designs with stock images so the client can see our vision. We typically take pictures after the website launch to use their images with our vision. Lorem Ipsum is fine for paragraphs, but we ask that you write the headers in correct English. We want to be able to show the vision and identify the sections of the website.

INSPIRATION:
We typically add a couple of links in the brief of websites we like to help you get started in your design.

REVISIONS:
We do not often ask for revisions of the designs unless we see something in the design that may not appeal to the client. If there are slight changes that we want to make, we do that in the development process.

FEEDBACK:
We rarely give feedback on designs during the design process. We are working on many website projects and do not have the time to provide feedback. We usually respond if your request is well thought out and asks specific questions, but a note asking “feedback, please” usually goes unanswered.

```html
<!DOCTYPE html>
<html lang="en">
<head>
<meta charset="utf-8">
<title>Harbor Tidy Squad — Commercial Cleaning</title>
<link href="https://fonts.googleapis.com/css2?family=Montserrat:wght@600;700;800&family=Lato:wght@400;700&display=swap" rel="stylesheet">
<style>
:root{
  --blue:#1b4fc2;
  --navy:#0b5aa8;
  --red:#e3251b;
  --gold:#f2a81d;
  --ink:#1d1d1f;
  --body:#444a55;
  --tint:#eef3fb;
  --white:#fff;
}
*{margin:0;padding:0;box-sizing:border-box}
html,body{width:1200px;height:3765px;overflow:hidden}
body{font-family:'Lato',sans-serif;color:var(--ink);background:var(--white);position:relative}
.abs{position:absolute}
.btn{position:absolute;background:var(--red);color:var(--white);font-weight:700;font-size:17px;display:flex;align-items:center;justify-content:center;border-radius:3px}
.h2{font-family:'Montserrat',sans-serif;font-weight:700;color:var(--blue);font-size:40px}
.bar{position:absolute;height:4px;width:86px;background:var(--gold);border-radius:2px}
.center{left:0;width:1200px;text-align:center}
/* header */
.site-header{position:absolute;top:0;left:0;width:1200px;height:86px;background:var(--white)}
.brand{position:absolute;display:flex;align-items:center;gap:12px;font-family:'Lato',sans-serif;font-weight:700;font-size:22px;letter-spacing:3px;color:var(--blue)}
.brand i{width:22px;height:22px;border-radius:50%;background:var(--red);display:block}
.nav a{position:absolute;top:31px;font-size:16px;color:var(--ink);text-decoration:none}
.nav a.active{color:var(--blue);text-decoration:underline}
/* hero */
.hero{position:absolute;top:86px;left:0;width:1200px;height:519px;
  background:
    linear-gradient(90deg,rgba(30,32,36,.72) 0%,rgba(30,32,36,.45) 38%,rgba(30,32,36,0) 62%),
    linear-gradient(180deg,#9a9ea3 0%,#b9b9b6 30%,#8e8b86 62%,#cfcac2 82%,#a8a49c 100%)}
.hero::after{content:"";position:absolute;right:0;top:0;width:520px;height:519px;background:linear-gradient(100deg,rgba(0,0,0,0) 0%,rgba(40,40,44,.35) 45%,rgba(70,70,74,.15) 100%)}
.hero h1{position:absolute;left:108px;top:100px;font-family:'Montserrat',sans-serif;font-weight:700;font-size:54px;line-height:64px;color:var(--white);z-index:1}
.hero p{position:absolute;left:112px;top:232px;width:560px;font-size:17px;line-height:26px;font-weight:700;color:var(--white);z-index:1}
.hero .btn{z-index:1}
/* about */
.photo{position:absolute;border-radius:6px;box-shadow:0 2px 6px rgba(0,0,0,.12)}
.about p{position:absolute;left:642px;width:446px;font-size:15px;line-height:25px;color:var(--body);text-align:justify}
/* services */
.services{position:absolute;top:1177px;left:0;width:1200px;height:543px;background:var(--tint)}
.card{position:absolute;background:var(--white);border:1px solid #dde3ec;border-radius:4px;box-shadow:0 2px 8px rgba(0,0,0,.06);text-align:center}
.card h3{font-weight:700;font-size:20px;margin-top:124px;color:var(--ink)}
.card p{font-size:14.5px;line-height:25px;color:var(--body);margin:12px auto 0;width:260px;height:75px;overflow:hidden}
.card a{display:block;font-size:13.5px;font-style:italic;text-decoration:underline;color:var(--ink);margin-top:12px}
.card .svc-icon{position:absolute;left:50%;margin-left:-38px;top:20px}
.arrow{position:absolute;width:28px;height:28px;border:1.5px solid #333;border-radius:50%;display:flex;align-items:center;justify-content:center}
/* why */
.why-item{position:absolute;left:112px;width:440px}
.why-item .ic{position:absolute;left:0;top:2px}
.why-item h4{position:absolute;left:86px;top:0;font-size:17.5px;font-weight:700}
.why-item p{position:absolute;left:87px;top:30px;width:352px;font-size:14.5px;line-height:25px;color:var(--body);height:50px;overflow:hidden}
/* cta */
.cta{position:absolute;top:2450px;left:0;width:1200px;height:371px;background:linear-gradient(90deg,#e8e8f3,#dfe1ef)}
.cta p{position:absolute;left:560px;top:170px;width:520px;text-align:center;font-size:16.5px;line-height:25px;color:var(--ink)}
/* testimonials */
.quote{position:absolute;top:2994px;width:309px;height:275px;background:var(--white);border:1px solid #dde3ec;border-radius:4px;box-shadow:0 2px 8px rgba(0,0,0,.06)}
.quote .stars{position:absolute;left:22px;top:26px;display:flex;gap:2px}
.quote p{position:absolute;left:22px;top:64px;width:264px;height:75px;overflow:hidden;font-size:15px;line-height:25px;color:#555}
.quote a{position:absolute;left:22px;top:149px;font-size:14px;font-style:italic;text-decoration:underline;color:var(--ink)}
.quote .av{position:absolute;left:28px;top:180px;width:78px;height:78px;border-radius:50%}
.quote h5{position:absolute;left:126px;top:196px;font-size:19px;font-weight:700}
.quote span{position:absolute;left:126px;top:228px;font-size:14px;color:#333}
/* footer */
.footer{position:absolute;top:3355px;left:0;width:1200px;height:410px;background:var(--navy);color:var(--white)}
.footer h6{position:absolute;top:80px;font-size:19px;font-weight:700}
.footer h6::after{content:"";position:absolute;left:0;top:34px;width:80px;height:2px;background:var(--white)}
.flist{position:absolute;top:138px;list-style:none}
.flist li{font-size:14.5px;height:34px;position:relative;padding-left:23px}
.flist li::before{content:"";position:absolute;left:0;top:7px;width:7px;height:7px;border-radius:50%;background:var(--white)}
.contact-row{position:absolute;left:880px;display:flex;gap:10px;font-size:15px;line-height:24px}
.contact-row svg{flex:none;margin-top:4px}
</style>
</head>
<body>

<svg width="0" height="0" style="position:absolute">
  <defs>
    <linearGradient id="duo" x1="0" y1="0" x2="1" y2="1">
      <stop offset="0" stop-color="#1b4fc2"/><stop offset="1" stop-color="#e3251b"/>
    </linearGradient>
    <path id="star" d="M9 1l2.4 5 5.4.6-4 3.7 1.1 5.4L9 13l-4.9 2.7 1.1-5.4-4-3.7 5.4-.6z" fill="#f2a81d"/>
  </defs>
</svg>

<header class="site-header">
  <div class="brand" style="left:112px;top:30px"><i></i>HARBOR TIDY SQUAD</div>
  <nav class="nav">
    <a class="active" style="left:503px">Home</a>
    <a style="left:580px">About</a>
    <a style="left:655px">Services</a>
    <a style="left:746px">Industries</a>
    <a style="left:849px">Pricing</a>
  </nav>
  <div class="btn" style="left:949px;top:20px;width:139px;height:46px">Contact Us</div>
</header>

<section class="hero" role="img" aria-label="Cleaner in uniform operating a floor scrubbing machine in a bright modern office lobby">
  <h1>Clean Spaces<br>Confident Businesses</h1>
  <p>Reliable, insured commercial cleaning for offices, healthcare, retail, and industrial spaces — done right, every time.</p>
  <div class="btn" style="left:112px;top:312px;width:170px;height:46px">Get a Free Quote</div>
</section>

<section class="about">
  <div class="photo" style="left:112px;top:691px;width:215px;height:194px;background:linear-gradient(170deg,#7f9fc2 0%,#b9cde0 45%,#dfe8ef 70%,#8fa7bd 100%)" role="img" aria-label="Worker mopping a warehouse floor"></div>
  <div class="photo" style="left:342px;top:691px;width:216px;height:194px;background:linear-gradient(150deg,#6e6258 0%,#c7b8a6 40%,#e6e0d8 65%,#9b9892 100%)" role="img" aria-label="Cleaner spraying and wiping a steel counter"></div>
  <div class="photo" style="left:112px;top:897px;width:215px;height:194px;background:linear-gradient(120deg,#6f97b8 0%,#a9c9df 40%,#d6e7f1 60%,#4f7391 100%)" role="img" aria-label="Worker pressure washing a building facade"></div>
  <div class="photo" style="left:342px;top:897px;width:216px;height:194px;background:linear-gradient(200deg,#3f3a35 0%,#8a7d6e 35%,#d9cfc2 65%,#7a6f63 100%)" role="img" aria-label="Floor polishing machine on a shiny floor"></div>
  <svg class="abs" style="left:280px;top:834px" width="108" height="108"><circle cx="54" cy="54" r="50" fill="none" stroke="#fff" stroke-width="3"/><circle cx="16" cy="26" r="4" fill="#fff"/><circle cx="92" cy="82" r="4" fill="#fff"/></svg>
  <h2 class="h2 abs" style="left:641px;top:680px">About Us</h2>
  <div class="bar" style="left:642px;top:742px"></div>
  <p style="top:768px">Harbor Tidy Squad is a trusted commercial cleaning company serving offices, healthcare facilities, retail spaces, and industrial sites across [City/Region]. We believe that a clean environment is the foundation of a productive business — and we take that responsibility seriously.</p>
  <p style="top:905px">Every member of our crew is fully trained, background-checked, and committed to delivering excellence with integrity and attention to detail. From nightly janitorial work to specialized disinfection, we tailor every service plan to meet your facility’s exact needs.</p>
  <div class="btn" style="left:642px;top:1025px;width:127px;height:47px">Read More</div>
</section>

<section class="services">
  <h2 class="h2 abs center" style="top:70px">Our Services</h2>
  <div class="bar" style="left:557px;top:133px"></div>
  <div class="arrow" style="left:41px;top:300px"><svg width="10" height="12"><path d="M7 1 2 6l5 5" fill="none" stroke="#333" stroke-width="1.5"/></svg></div>
  <div class="arrow" style="left:1133px;top:300px"><svg width="10" height="12"><path d="M3 1l5 5-5 5" fill="none" stroke="#333" stroke-width="1.5"/></svg></div>

  <div class="card" style="left:112px;top:174px;width:309px;height:281px">
    <svg class="svc-icon" width="76" height="80" viewBox="0 0 76 80" role="img" aria-label="Floor cleaning machine icon">
      <path d="M18 8v46" stroke="#1b4fc2" stroke-width="5" stroke-linecap="round"/>
      <path d="M18 30l22 18" stroke="#1b4fc2" stroke-width="4" stroke-linecap="round"/>
      <rect x="36" y="46" width="30" height="18" rx="4" fill="#e3251b"/>
      <rect x="42" y="40" width="18" height="8" rx="2" fill="#e3251b"/>
      <circle cx="44" cy="68" r="5" fill="#1b4fc2"/><circle cx="60" cy="68" r="5" fill="#1b4fc2"/>
      <path d="M10 74h60" stroke="#e3251b" stroke-width="3" stroke-linecap="round"/>
    </svg>
    <h3>Office Cleaning</h3>
    <p>Keep your workplace clean, fresh, and productive with daily or weekly office cleaning programs.</p>
    <a>Learn More</a>
  </div>

  <div class="card" style="left:445px;top:174px;width:309px;height:281px">
    <svg class="svc-icon" width="76" height="80" viewBox="0 0 76 80" role="img" aria-label="Sanitizing spray and medical cross icon">
      <circle cx="34" cy="44" r="26" fill="url(#duo)"/>
      <path d="M22 44l8 8 16-16" fill="none" stroke="#fff" stroke-width="5" stroke-linecap="round" stroke-linejoin="round"/>
      <path d="M64 6v12M58 12h12" stroke="#e3251b" stroke-width="3" stroke-linecap="round"/>
      <path d="M64 64v10M59 69h10" stroke="#e3251b" stroke-width="3" stroke-linecap="round"/>
      <path d="M8 14l8 4M6 24h9M10 6l6 7" stroke="#1b4fc2" stroke-width="3" stroke-linecap="round"/>
    </svg>
    <h3>Medical &amp; Healthcare Cleaning</h3>
    <p>Maintain the highest hygiene standards with OSHA- and CDC-compliant medical cleaning.</p>
    <a>Learn More</a>
  </div>

  <div class="card" style="left:779px;top:174px;width:309px;height:281px">
    <svg class="svc-icon" width="76" height="80" viewBox="0 0 76 80" role="img" aria-label="Storefront with awning icon">
      <rect x="12" y="6" width="52" height="8" rx="2" fill="#1b4fc2"/>
      <path d="M8 16h60l-4 14H12z" fill="#1b4fc2"/>
      <path d="M20 16v14M32 16v14M44 16v14M56 16v14" stroke="#fff" stroke-width="2"/>
      <rect x="12" y="32" width="52" height="36" fill="#e3251b"/>
      <rect x="18" y="40" width="14" height="28" fill="#fff"/>
      <rect x="38" y="40" width="20" height="14" fill="#fff"/>
      <path d="M6 70h64" stroke="#1b4fc2" stroke-width="4" stroke-linecap="round"/>
    </svg>
    <h3>Retail &amp; Storefront Cleaning</h3>
    <p>Create a spotless shopping experience that keeps customers coming back. Includes: front-of-house cleaning, glass</p>
    <a>Learn More</a>
  </div>
</section>

<section class="why">
  <h2 class="h2 abs center" style="top:1792px">Why Choose Us</h2>
  <div class="bar" style="left:557px;top:1854px"></div>

  <div class="why-item" style="top:1905px">
    <svg class="ic" width="54" height="54" viewBox="0 0 54 54" role="img" aria-label="Shield in hand icon">
      <path d="M30 4l12 5v9c0 8-5 13-12 16-7-3-12-8-12-16V9z" fill="none" stroke="#1b4fc2" stroke-width="2.5"/>
      <path d="M24 18l5 5 8-8" fill="none" stroke="#1b4fc2" stroke-width="2.5" stroke-linecap="round"/>
      <path d="M4 38h10l12 6h14l8-6" fill="none" stroke="#e3251b" stroke-width="2.5" stroke-linecap="round" stroke-linejoin="round"/>
      <rect x="2" y="34" width="6" height="16" fill="#e3251b"/>
    </svg>
    <h4>Reliable &amp; Consistent Service</h4><p>You can count on us to show up on time and deliver spotless results — every single visit.</p>
  </div>
  <div class="why-item" style="top:2007px">
    <svg class="ic" width="54" height="54" viewBox="0 0 54 54" role="img" aria-label="Staff badge icon">
      <rect x="10" y="8" width="34" height="42" rx="4" fill="none" stroke="#e3251b" stroke-width="2.5"/>
      <rect x="20" y="4" width="14" height="8" rx="2" fill="#1b4fc2"/>
      <circle cx="27" cy="24" r="6" fill="none" stroke="#1b4fc2" stroke-width="2.5"/>
      <path d="M17 42c2-6 6-8 10-8s8 2 10 8" fill="none" stroke="#1b4fc2" stroke-width="2.5"/>
    </svg>
    <h4>Professionally Trained Staff</h4><p>Every cleaner is background-checked, uniformed, and trained to handle commercial environments safely and</p>
  </div>
  <div class="why-item" style="top:2109px">
    <svg class="ic" width="54" height="54" viewBox="0 0 54 54" role="img" aria-label="Insurance shield icon">
      <path d="M27 4l16 6v12c0 11-7 18-16 22-9-4-16-11-16-22V10z" fill="none" stroke="#1b4fc2" stroke-width="2.5"/>
      <path d="M20 24l6 6 10-11" fill="none" stroke="#e3251b" stroke-width="3" stroke-linecap="round"/>
      <path d="M4 40l8 10M50 40l-8 10" stroke="#e3251b" stroke-width="2.5" stroke-linecap="round"/>
    </svg>
    <h4>Fully Insured &amp; Compliant</h4><p>Your peace of mind matters. We’re fully bonded and insured, and our cleaning methods meet OSHA and</p>
  </div>
  <div class="why-item" style="top:2211px">
    <svg class="ic" width="54" height="54" viewBox="0 0 54 54" role="img" aria-label="Eco leaf icon">
      <path d="M10 44c0-18 12-28 32-30-2 20-12 30-30 30z" fill="none" stroke="#e3251b" stroke-width="2.5"/>
      <path d="M12 42l20-18" stroke="#e3251b" stroke-width="2.5" stroke-linecap="round"/>
      <path d="M14 10a18 18 0 0 1 26 0M40 10l1-6M40 10l-6 1" fill="none" stroke="#1b4fc2" stroke-width="2.5" stroke-linecap="round"/>
    </svg>
    <h4>Eco-Friendly Options</h4><p>You can count on us to show up on time and deliver spotless results — every single visit.</p>
  </div>

  <div class="btn" style="left:113px;top:2318px;width:127px;height:46px">View More</div>
  <div class="photo" style="left:643px;top:1907px;width:445px;height:459px;background:linear-gradient(165deg,#d8dcd6 0%,#7f9a72 25%,#4a5d44 50%,#6d7378 75%,#b9bcbf 100%)" role="img" aria-label="Cleaning team vacuuming and mopping a modern office"></div>
</section>

<section class="cta">
  <div class="abs" style="left:0;top:0;width:545px;height:371px;background:linear-gradient(180deg,#e6e8f2 0%,#d9dff0 30%,#2c62c9 55%,#1c4bb0 80%,#3a3f52 100%)" role="img" aria-label="Smiling cleaning team in blue uniforms holding cleaning supplies"></div>
  <h2 class="h2 abs" style="left:560px;width:520px;text-align:center;top:84px">Ready to Get Started?</h2>
  <div class="bar" style="left:776px;top:144px"></div>
  <p>Let Harbor Tidy Squad handle the dirt — so you can focus on your business. Fast quotes, flexible schedules, and guaranteed satisfaction.</p>
  <div class="btn" style="left:727px;top:240px;width:170px;height:46px">Get a Free Quote</div>
</section>

<section class="testimonials">
  <h2 class="h2 abs center" style="top:2892px">What Our Clients Say</h2>
  <div class="bar" style="left:557px;top:2954px"></div>
  <div class="arrow" style="left:41px;top:3118px"><svg width="10" height="12"><path d="M7 1 2 6l5 5" fill="none" stroke="#333" stroke-width="1.5"/></svg></div>
  <div class="arrow" style="left:1133px;top:3118px"><svg width="10" height="12"><path d="M3 1l5 5-5 5" fill="none" stroke="#333" stroke-width="1.5"/></svg></div>
  <div class="quote" style="left:112px">
    <div class="stars"><svg width="18" height="17"><use href="#star"/></svg><svg width="18" height="17"><use href="#star"/></svg><svg width="18" height="17"><use href="#star"/></svg><svg width="18" height="17"><use href="#star"/></svg><svg width="18" height="17"><use href="#star"/></svg></div>
    <p>“Harbor Tidy Squad has been maintaining our office for over two years, and the difference is night and day.</p>
    <a>Read More</a><div class="av" style="background:linear-gradient(160deg,#6d6f73,#c98a55)" role="img" aria-label="Client portrait"></div><h5>Dana Whitfield</h5><span>Office Manager</span>
  </div>
  <div class="quote" style="left:445px">
    <div class="stars"><svg width="18" height="17"><use href="#star"/></svg><svg width="18" height="17"><use href="#star"/></svg><svg width="18" height="17"><use href="#star"/></svg><svg width="18" height="17"><use href="#star"/></svg><svg width="18" height="17"><use href="#star"/></svg></div>
    <p>We needed a cleaning partner who understood healthcare-level hygiene. Harbor Tidy Squad’s staff follow</p>
    <a>Read More</a><div class="av" style="background:linear-gradient(160deg,#e4e2dd,#a7896b)" role="img" aria-label="Client portrait"></div><h5>Dr. Arun Mehta</h5><span>Director</span>
  </div>
  <div class="quote" style="left:779px">
    <div class="stars"><svg width="18" height="17"><use href="#star"/></svg><svg width="18" height="17"><use href="#star"/></svg><svg width="18" height="17"><use href="#star"/></svg><svg width="18" height="17"><use href="#star"/></svg><svg width="18" height="17"><use href="#star"/></svg></div>
    <p>Our storefront has never looked this good. From the windows to the floors, they make sure everything</p>
    <a>Read More</a><div class="av" style="background:linear-gradient(160deg,#e9eaec,#e27a22)" role="img" aria-label="Client portrait"></div><h5>Nora Castell</h5><span>Store Owner</span>
  </div>
</section>

<footer class="footer">
  <div class="brand" style="left:112px;top:100px;color:var(--white);font-size:20px"><i style="background:var(--white)"></i>HARBOR TIDY SQUAD</div>
  <div class="abs" style="left:112px;top:194px;width:221px;height:42px;background:var(--white);border-radius:2px;color:#333;font-size:14.5px;padding:13px 22px">Email</div>
  <div class="btn" style="left:112px;top:249px;width:118px;height:43px">Subscribe</div>
  <h6 style="left:420px">Quick Links</h6>
  <ul class="flist" style="left:421px"><li>Home</li><li>About Us</li><li>Services</li><li>Why Choose Us</li><li>Testimonials</li></ul>
  <h6 style="left:607px">Services</h6>
  <ul class="flist" style="left:608px"><li>Office Cleaning</li><li>Janitorial Services</li><li>Window &amp; Glass Cleaning</li><li>Floor &amp; Carpet Care</li><li>Post-Construction Cleaning</li><li>Industrial / Warehouse Cleaning</li></ul>
  <h6 style="left:882px">Contact Us</h6>
  <div class="contact-row" style="top:124px"><svg width="16" height="18"><path d="M8 1a6 6 0 0 0-6 6c0 4.5 6 10 6 10s6-5.5 6-10a6 6 0 0 0-6-6zm0 8.3A2.3 2.3 0 1 1 8 4.7a2.3 2.3 0 0 1 0 4.6z" fill="#fff"/></svg><span>220 Dockside Ave,<br>Portmere, CA 95201</span></div>
  <div class="contact-row" style="top:196px"><svg width="16" height="16"><circle cx="8" cy="8" r="8" fill="#fff"/><path d="M4 5.5h8v5H4z M4 5.5l4 3 4-3" fill="none" stroke="#0b5aa8" stroke-width="1.2"/></svg><span>info@harbortidysquad.com</span></div>
  <div class="contact-row" style="top:242px"><svg width="16" height="16"><circle cx="8" cy="8" r="8" fill="#fff"/><path d="M5 4.5c.5 3 2.5 5.8 6.5 7l.8-1.6-1.8-1-1 .8c-1-.6-1.8-1.4-2.3-2.4l.8-1-1-1.8z" fill="#0b5aa8"/></svg><span>+1 555 014 2290</span></div>
  <div class="abs" style="left:112px;top:359px;width:976px;height:1px;background:rgba(255,255,255,.45)"></div>
  <div class="abs" style="left:112px;top:374px;width:20px;height:20px;border-radius:50%;background:var(--white)" role="img" aria-label="Social profile link"></div>
  <div class="abs" style="left:148px;top:374px;width:20px;height:20px;border-radius:50%;background:var(--white)" role="img" aria-label="Social profile link"></div>
  <div class="abs" style="left:700px;top:376px;width:388px;text-align:right;font-size:14.5px">© 2025 Harbor Tidy Squad. All Rights Reserved.</div>
</footer>

</body>
</html>
```